A colorful, playful, nerdy, creative logo for a business analytics and marketing analytics company.

We need a logo and website design for a new company based in Florida called Brightfold Pattern Works Collective. We provide marketing, consumer and business insights through the use of market research, business analytics and marketing analytics. We are a collection of several individuals each with specific expertise and come together to provide the best possible insights about their consumers/guests/customers. We would like to see a design that uses colors that show a free spirit but deeply rooted in analytics " a super nerd " Along those steps, we would like to see either a playful, nerdy, creative logo or one that includes the full or partial name of the company. We have simplified our "brand" by saying when you initially start with us you may have several questions "?" through the process of learning about your consumers/brand ">" incredible solutions, strategies are developed "!" So something like a ?>! symbol would be interesting. Although the name of the company sounds very complex and very long to write, we would be interested in thoughtful ways of shorting the name or incorporating into the final logo design

Target Market(s)

Business or organizations that currently do not have an analytics/research function

Industry/Entity Type

Business

Contact Information for Business Card

Incorporate final logo and colors font. In the past, I have used a "wordle" website to show 10 common research terms scattered about .. showing them as strength or core competencies.

Logo Text

?>! or Brightfold Pattern Works Collective or BPW Collective

Coding

Coded - Design and coding required

Number of Pages Required

4 page

Font styles to use
Sans Serif
Decorative

Requirements
Must have
• The project must communicate analytics/scientific. It must we unique but not unique for the sack of being unique.
• It must either be a logo or a simple way to communicate the company name Brightfold Pattern Works Collective
Nice to have
• Again incorporating the symbols ?>! in that order. Showing confusion to gaining insights and then developing incredible solutions that are used to effect consumer behavior.
• Look to CPG ( consumer package goods) industry to input
Should not have
• I am pretty open to suggestions.

```html
<!DOCTYPE html>
<html lang="en">
<head>
<meta charset="utf-8">
<title>BPWC — Brightfold Pattern Works Collective</title>
<link rel="stylesheet" href="https://fonts.googleapis.com/css2?family=Play:wght@400;700&family=Quicksand:wght@400;500;600;700&display=swap">
<style>
:root{
  --orange:#ff6600;
  --orange-deep:#c2470b;
  --salmon:#f4805f;
  --salmon-light:#f7a183;
  --ink:#1f1f1f;
  --text:#444;
  --muted:#666;
  --light:#f1f1f1;
  --lavender:#ecebf6;
  --white:#fff;
  --dark:#333;
}
*{box-sizing:border-box;margin:0;padding:0}
html,body{width:1200px;height:3297px;overflow:hidden}
body{position:relative;background:var(--white);font-family:"Quicksand",sans-serif;color:var(--text)}
.abs{position:absolute}
.title{font-family:"Play",sans-serif;font-weight:700;font-size:42px;color:var(--orange-deep);text-align:center;left:0;width:1200px}
.title span{color:var(--orange)}

/* header */
.site-header{left:0;top:0;width:1200px;height:110px;background:var(--light)}
.brand{left:81px;top:18px}
.brand-mark{font-family:"Play",sans-serif;font-weight:700;font-size:64px;line-height:58px;color:var(--orange);letter-spacing:6px}
.brand-sub{font-size:9.5px;font-weight:600;color:var(--ink);margin-top:4px}
.nav a{position:absolute;top:33px;height:53px;line-height:53px;font-size:15px;color:var(--ink);text-decoration:none;font-weight:500}
.nav a.active{background:var(--orange);color:var(--white);padding:0 27px}

.hero{left:0;top:110px;width:1200px;height:417px;background:linear-gradient(180deg,#f58a66,#f47a55)}

/* about */
.about{left:0;top:527px;width:1200px;height:302px;background:#f6f6f6}
.about .title{top:50px}
.about .rule{left:583px;top:108px;width:34px;height:3px;background:var(--ink)}
.about p{left:120px;top:126px;width:960px;text-align:center;font-size:13.5px;line-height:23px;color:var(--ink)}

.cards{left:0;top:829px;width:1200px;height:239px;background:var(--salmon)}
.card{top:0;height:239px;width:398px;color:var(--white)}
.card.featured{left:398px;top:-2px;height:246px;width:402px;background:var(--orange);box-shadow:0 4px 10px rgba(0,0,0,.25);z-index:2}
.card .icon{left:72px;top:48px;width:80px;height:58px}
.card h3{left:180px;top:55px;font-family:"Play",sans-serif;font-size:19px;font-weight:700}
.card p{left:180px;top:92px;width:150px;font-size:12.5px;line-height:20px;color:var(--salmon-light)}
.card.featured h3{color:var(--ink)}
.card.featured p{color:var(--ink)}
.card .more{right:38px;top:165px;font-size:16px;font-weight:700;letter-spacing:.3px}
.card.featured .more{color:var(--ink)}

/* how it works */
.how{left:0;top:1068px;width:1200px;height:723px;background:var(--white)}
.how .title{top:50px}
.step h4{position:absolute;font-family:"Play",sans-serif;font-size:22px;font-weight:700;color:var(--ink);width:280px;text-align:center}
.step p{position:absolute;width:280px;text-align:center;font-size:13px;line-height:22px;color:var(--muted)}
.figure{border-radius:14px;background:#eeeef2}

/* services */
.services{left:0;top:1791px;width:1200px;height:521px;background:#ededed}
.services .title{top:60px}
.service{top:148px;width:271px;height:310px;background:#f7f7f7;border-top:4px solid #ccc;text-align:center}
.service.featured{background:var(--white);border-top-color:var(--orange)}
.service .badge{position:absolute;left:89px;top:22px;width:94px;height:94px;border-radius:50%;border:1px solid #ddd;background:var(--white)}
.service .badge svg{position:absolute;left:25px;top:25px}
.service h3{position:absolute;left:0;width:100%;top:146px;font-family:"Play",sans-serif;font-size:21px;font-weight:700;color:var(--orange-deep)}
.service.featured h3{color:var(--orange)}
.service p{position:absolute;left:20px;width:231px;top:182px;font-size:13px;line-height:23px;color:var(--muted)}

/* testimonials */
.clients{left:0;top:2312px;width:1200px;height:348px;background:var(--white)}
.clients .title{top:54px}
.quote-mark{left:578px;top:128px;font-family:"Play",sans-serif;font-size:80px;line-height:80px;color:#c8c8c8;font-weight:700}
.clients p{left:200px;top:184px;width:800px;text-align:center;font-size:13.5px;line-height:25px;color:var(--ink)}
.client-name{left:0;width:1200px;top:278px;text-align:center;font-size:12.5px;font-weight:600;color:var(--orange)}

/* contact */
.contact{left:0;top:2660px;width:1200px;height:488px;background:var(--light)}
.contact .title{top:50px}
.field{left:246px;width:312px;height:48px;background:var(--white);border:1px solid #ccc;font-size:12.5px;padding:14px 12px;color:#555}
.message{left:578px;top:149px;width:396px;height:180px;background:var(--white);border:1px solid #ccc;font-size:12.5px;padding:14px 12px;color:#555}
.submit{left:532px;top:351px;width:136px;height:51px;background:var(--orange);color:var(--white);font-weight:700;font-size:17px;text-align:center;line-height:51px}

/* footer */
.site-footer{left:0;top:3148px;width:1200px;height:149px;background:var(--orange)}
.social{top:-29px;width:58px;height:58px;border-radius:50%;background:var(--dark);border:4px solid var(--white)}
.social.first{background:var(--white);border-color:var(--orange)}
.footer-brand{left:81px;top:44px;font-family:"Play",sans-serif;font-weight:700;font-size:64px;line-height:64px;color:var(--white);letter-spacing:6px}
.newsletter{left:389px;top:61px;width:446px;height:48px;border-radius:24px;background:var(--white)}
.newsletter .ph{position:absolute;left:30px;top:15px;font-size:13px;font-style:italic;color:#777}
.newsletter .btn{position:absolute;right:0;top:0;width:191px;height:48px;border-radius:24px;background:var(--dark);color:var(--white);font-weight:700;font-size:19px;text-align:center;line-height:48px}
.copy{left:842px;top:68px;width:280px;font-size:12.5px;line-height:20px;color:var(--ink);text-align:right;font-weight:600}
</style>
</head>
<body>

<header class="abs site-header">
  <div class="abs brand">
    <div class="brand-mark">BPWC</div>
    <div class="brand-sub">Brightfold Pattern Works Collective</div>
  </div>
  <nav class="nav">
    <a class="active" style="left:459px">HOME</a>
    <a style="left:587px">ABOUT US</a>
    <a style="left:719px">SERVICES</a>
    <a style="left:844px">HOW IT WORKS</a>
    <a style="left:1013px">CONTACT US</a>
  </nav>
</header>

<section class="abs hero" role="img" aria-label="Flat illustration of creative workspace items: light bulbs with heart and star, laptop, monitor, brain in a box, drawing tablet and pencils"></section>

<section class="abs about">
  <h2 class="abs title">About <span>US</span></h2>
  <div class="abs rule"></div>
  <p class="abs">Lorem Ipsum is simply dummy text of the printing and typesetting industry. Lorem Ipsum has been the industry's standard dummy text ever since the 1500s, when an unknown printer took a galley of type and scrambled it to make a type specimen book. It has survived not only five centuries, but also the leap into electronic typesetting, remaining essentially unchanged. It was popularised in the 1960s with the release of Letraset sheets containing.</p>
</section>

<section class="abs cards">
  <article class="abs card" style="left:0">
    <svg class="abs icon" viewBox="0 0 80 58" aria-hidden="true"><path d="M8 22h14l30-16v46L22 36H8z" fill="#f9b59b"/><rect x="16" y="36" width="9" height="16" fill="#f9b59b"/><path d="M60 20l10-6M60 29h12M60 38l10 6" stroke="#f9b59b" stroke-width="4" stroke-linecap="round"/></svg>
    <h3 class="abs">Marketing</h3>
    <p class="abs">Lorem Ipsum is simply dummy text of the printing and typesetting industry.</p>
    <div class="abs more">READ MORE</div>
  </article>
  <article class="abs card featured">
    <svg class="abs icon" viewBox="0 0 80 58" aria-hidden="true" style="top:42px;height:80px"><circle cx="40" cy="30" r="24" fill="none" stroke="#111" stroke-width="5"/><circle cx="40" cy="30" r="13" fill="none" stroke="#111" stroke-width="5"/><circle cx="40" cy="30" r="5" fill="#111"/><rect x="35" y="40" width="10" height="18" rx="4" fill="#111"/></svg>
    <h3 class="abs">Consumer</h3>
    <p class="abs">Lorem Ipsum is simply dummy text of the printing and typesetting industry.</p>
    <div class="abs more">READ MORE</div>
  </article>
  <article class="abs card" style="left:800px">
    <svg class="abs icon" viewBox="0 0 80 58" aria-hidden="true"><path d="M4 22l16-10 14 6 12-6 16 4 14 8-12 18-18 6-18-10z" fill="#f9b59b"/></svg>
    <h3 class="abs">Business</h3>
    <p class="abs">Lorem Ipsum is simply dummy text of the printing and typesetting industry.</p>
    <div class="abs more">READ MORE</div>
  </article>
</section>

<section class="abs how">
  <svg class="abs" style="left:0;top:0" width="1200" height="723" aria-hidden="true">
    <defs><linearGradient id="wash" x1="0" y1="0" x2="0" y2="1"><stop offset="0" stop-color="#ffffff"/><stop offset="1" stop-color="#e8e7f5"/></linearGradient></defs>
    <path d="M0 0H1200V262C1150 255 1080 229 1002 229C900 229 830 334 736 334C640 334 580 147 466 147C360 147 300 340 198 356C150 365 100 350 0 321Z" fill="url(#wash)"/>
    <path d="M0 321C100 350 150 365 198 356C300 340 360 147 466 147C580 147 640 334 736 334C830 334 900 229 1002 229C1080 229 1150 255 1200 262" fill="none" stroke="#c2470b" stroke-width="3" stroke-dasharray="1 8" stroke-linecap="round"/>
    <g fill="#fff" stroke-width="4"><circle cx="198" cy="356" r="9" stroke="#ff6600"/><circle cx="466" cy="150" r="9" stroke="#2b2f5a"/><circle cx="736" cy="334" r="9" stroke="#2b2f5a"/><circle cx="1002" cy="229" r="9" stroke="#2b2f5a"/></g>
    <g fill="#ff6600"><circle cx="198" cy="356" r="3"/></g><g fill="#2b2f5a"><circle cx="466" cy="150" r="3"/><circle cx="736" cy="334" r="3"/><circle cx="1002" cy="229" r="3"/></g>
  </svg>
  <h2 class="abs title">How <span>It Works</span></h2>

  <div class="step">
    <div class="abs figure" style="left:153px;top:394px;width:90px;height:125px" role="img" aria-label="Sketch of a puzzled figure with a red question mark"></div>
    <h4 style="left:58px;top:602px">Client's Problem</h4>
    <p style="left:58px;top:638px">Lorem Ipsum is simply dummy text of the printing and typesetting industry.</p>
  </div>
  <div class="step">
    <div class="abs figure" style="left:421px;top:185px;width:90px;height:154px" role="img" aria-label="Sketch of a thinking figure with blue gears"></div>
    <h4 style="left:302px;top:397px">Contact Us</h4>
    <p style="left:302px;top:433px">Lorem Ipsum is simply dummy text of the printing and typesetting industry.</p>
  </div>
  <div class="step">
    <div class="abs figure" style="left:691px;top:372px;width:90px;height:187px" role="img" aria-label="Sketch of a figure pointing up at a yellow light bulb"></div>
    <h4 style="left:596px;top:586px">Solution</h4>
    <p style="left:596px;top:622px">Lorem Ipsum is simply dummy text of the printing and typesetting industry.</p>
  </div>
  <div class="step">
    <div class="abs figure" style="left:957px;top:251px;width:90px;height:154px" role="img" aria-label="Sketch of a cheerful figure under a green exclamation mark"></div>
    <h4 style="left:862px;top:476px">Happy Clients</h4>
    <p style="left:862px;top:512px">Lorem Ipsum is simply dummy text of the printing and typesetting industry.</p>
  </div>
</section>

<section class="abs services">
  <h2 class="abs title">Services <span>We Provide</span></h2>
  <article class="abs service" style="left:193px">
    <div class="badge"><svg width="44" height="44" viewBox="0 0 44 44" aria-hidden="true" fill="none" stroke="#ff6600" stroke-width="2.5"><polyline points="2,24 10,24 15,14 21,30 26,20 42,20"/><circle cx="22" cy="20" r="11"/><line x1="30" y1="28" x2="40" y2="40"/></svg></div>
    <h3>Market Research</h3>
    <p>Lorem Ipsum is simply dummy text of the printing and type setting industry.</p>
  </article>
  <article class="abs service featured" style="left:464px">
    <div class="badge"><svg width="44" height="44" viewBox="0 0 44 44" aria-hidden="true" fill="none" stroke="#ff6600" stroke-width="2.5"><polyline points="4,4 4,40 42,40"/><polyline points="8,34 16,22 24,28 34,12"/><polyline points="28,12 34,12 34,18"/></svg></div>
    <h3>Business Analytics</h3>
    <p>Lorem Ipsum is simply dummy text of the printing and type setting industry.</p>
  </article>
  <article class="abs service" style="left:735px">
    <div class="badge"><svg width="44" height="44" viewBox="0 0 44 44" aria-hidden="true"><rect x="3" y="5" width="38" height="26" fill="none" stroke="#ff6600" stroke-width="2.5"/><rect x="9" y="19" width="4" height="8" fill="#ff6600"/><rect x="15" y="14" width="4" height="13" fill="#ff6600"/><circle cx="31" cy="18" r="6" fill="#ff6600"/><path d="M14 31l-5 11M30 31l5 11M22 31v9" stroke="#ff6600" stroke-width="2.5"/></svg></div>
    <h3>Marketing Analytics</h3>
    <p>Lorem Ipsum is simply dummy text of the printing and type setting industry.</p>
  </article>
</section>

<section class="abs clients">
  <h2 class="abs title">Our <span>Happy Clients</span></h2>
  <div class="abs quote-mark">&ldquo;</div>
  <svg class="abs" style="left:132px;top:188px" width="20" height="44" aria-hidden="true"><polyline points="18,2 3,22 18,42" fill="none" stroke="#f08a60" stroke-width="2"/></svg>
  <svg class="abs" style="left:1048px;top:188px" width="20" height="44" aria-hidden="true"><polyline points="2,2 17,22 2,42" fill="none" stroke="#f08a60" stroke-width="2"/></svg>
  <p class="abs">Lorem Ipsum is simply dummy text of the printing and typesetting industry. Lorem Ipsum has been the industry's standard dummy text ever since the 1500s, when an unknown printer took a galley of type and scrambled it to make a type specimen book.</p>
  <div class="abs client-name">- CLIENT NAME</div>
</section>

<section class="abs contact">
  <h2 class="abs title">Keep <span>In Touch</span></h2>
  <div class="abs field" style="top:149px">Enter Name</div>
  <div class="abs field" style="top:215px">Enter Email</div>
  <div class="abs field" style="top:281px">Enter Contact No.</div>
  <div class="abs message">Enter Message</div>
  <div class="abs submit">SUBMIT</div>
</section>

<footer class="abs site-footer">
  <div class="abs social first" style="left:461px" role="img" aria-label="Social link one"></div>
  <div class="abs social" style="left:534px" role="img" aria-label="Social link two"></div>
  <div class="abs social" style="left:606px" role="img" aria-label="Social link three"></div>
  <div class="abs social" style="left:679px" role="img" aria-label="Social link four"></div>
  <div class="abs footer-brand">BPWC</div>
  <div class="abs newsletter"><span class="ph">E-mail</span><span class="btn">SUBSCRIBE</span></div>
  <div class="abs copy">© Brightfold Pattern Works Collective<br>- 2017. All Rights Reserved.</div>
</footer>

</body>
</html>
```